Business Card Design for Venture Kite

Venture Kite is a pro bono student consultancy service offered by Corvala KTRB to social start ups and enterprises. We provide consulting services with expertise in areas such as Marketing, IT, Business Strategy and Innovation.
I have attached\ the Venture Kite Logo here for your perusal.
Industry/Entity Type
Business
Contact Information for Business Card
Name: Ha Min Park Name: Thomas Leung
Role: Project Leader Role: Vice Project Leader
M:0477203941 M: 0479352806
E: ha-min.park@corvalaktrb.org E: thomas.leung@corvalaktrb.org
W: www.corvalaktrb.org W: www.corvalaktrb.org

```html
<!DOCTYPE html>
<html lang="en">
<head>
<meta charset="utf-8">
<title>Venture Kite – Business Card</title>
<link rel="stylesheet" href="https://fonts.googleapis.com/css2?family=Arimo:wght@400;700&family=Quicksand:wght@500&display=swap">
<style>
  :root {
    --page-bg: #e8eaed;
    --card-white: #ffffff;
    --amber-light: #ffbb16;
    --amber: #ffa200;
    --orange: #ff8c00;
    --orange-deep: #f47512;
    --ink: #1b1b1b;
    --ink-soft: #2a2a2a;
  }
  * { margin: 0; padding: 0; box-sizing: border-box; }
  html, body {
    width: 1000px;
    height: 1200px;
    overflow: hidden;
    background: var(--page-bg);
  }
  body { position: relative; font-family: "Arimo", Arial, sans-serif; color: var(--ink); }

  .card {
    position: absolute;
    left: 60px;
    width: 880px;
    height: 500px;
    background: var(--card-white);
    box-shadow: 0 6px 18px rgba(0,0,0,0.18);
    overflow: hidden;
  }
  .card--front { top: 70px; }
  .card--back { top: 630px; }

  .card__bands { position: absolute; inset: 0; width: 880px; height: 500px; }

  .brand-name {
    position: absolute;
    font-family: "Arimo", Arial, sans-serif;
    font-weight: 700;
    color: var(--ink);
    letter-spacing: -1px;
    line-height: 1;
    white-space: nowrap;
  }
  .card--front .brand-name {
    top: 150px;
    left: 0;
    width: 880px;
    text-align: center;
    font-size: 76px;
  }

  .tagline {
    position: absolute;
    top: 262px;
    left: 0;
    width: 880px;
    text-align: center;
    font-size: 31px;
    color: var(--ink-soft);
  }

  .services {
    position: absolute;
    top: 318px;
    left: 0;
    width: 880px;
    display: flex;
    justify-content: center;
    gap: 46px;
    list-style: none;
    font-size: 25px;
    color: var(--ink-soft);
  }
  .services li { display: flex; align-items: center; gap: 12px; }
  .services li::before {
    content: "";
    width: 8px;
    height: 8px;
    border-radius: 50%;
    background: var(--orange);
  }

  .card--back .brand-name {
    top: 222px;
    left: 56px;
    font-size: 54px;
  }

  .contacts {
    position: absolute;
    top: 112px;
    left: 488px;
    display: flex;
    flex-direction: column;
    gap: 22px;
  }
  .contact__name {
    font-family: "Quicksand", "Arimo", sans-serif;
    font-weight: 500;
    font-size: 28px;
    color: var(--orange);
    line-height: 1.1;
  }
  .contact__line {
    font-size: 17px;
    line-height: 1.3;
    color: var(--ink-soft);
  }

  .website {
    position: absolute;
    right: 40px;
    top: 430px;
    font-size: 20px;
    font-weight: 700;
    color: var(--card-white);
    letter-spacing: 0.5px;
  }
</style>
</head>
<body>
  <svg width="0" height="0" style="position:absolute" aria-hidden="true">
    <defs>
      <linearGradient id="band-top" x1="0" y1="0" x2="0" y2="1">
        <stop offset="0" stop-color="#ffbb16"/>
        <stop offset="1" stop-color="#ffa200"/>
      </linearGradient>
      <linearGradient id="band-bottom" x1="0" y1="0" x2="0" y2="1">
        <stop offset="0" stop-color="#ff8c00"/>
        <stop offset="1" stop-color="#f47512"/>
      </linearGradient>
    </defs>
  </svg>

  <section class="card card--front" aria-label="Card front">
    <svg class="card__bands" viewBox="0 0 880 500" aria-hidden="true">
      <polygon points="0,0 880,0 880,62 440,62 400,102 0,102" fill="url(#band-top)"/>
      <polyline points="0,88 394,88 434,48 880,48" fill="none" stroke="#ffffff" stroke-width="4"/>
      <polygon points="0,412 478,412 520,370 880,370 880,500 0,500" fill="url(#band-bottom)"/>
      <polyline points="0,428 484,428 526,386 880,386" fill="none" stroke="#ffffff" stroke-width="4"/>
      <line x1="0" y1="462" x2="880" y2="462" stroke="#ffffff" stroke-width="4"/>
    </svg>
    <div class="brand-name">Venture Kite</div>
    <p class="tagline">consulting services with expertise</p>
    <ul class="services">
      <li>Marketing</li>
      <li>IT</li>
      <li>Business Strategy</li>
      <li>Innovation</li>
    </ul>
  </section>

  <section class="card card--back" aria-label="Card back">
    <svg class="card__bands" viewBox="0 0 880 500" aria-hidden="true">
      <polygon points="0,0 880,0 880,62 440,62 400,102 0,102" fill="url(#band-top)"/>
      <polyline points="0,88 394,88 434,48 880,48" fill="none" stroke="#ffffff" stroke-width="4"/>
      <polygon points="0,412 578,412 620,370 880,370 880,500 0,500" fill="url(#band-bottom)"/>
      <polyline points="0,428 584,428 626,386 880,386" fill="none" stroke="#ffffff" stroke-width="4"/>
      <line x1="0" y1="470" x2="560" y2="470" stroke="#ffffff" stroke-width="4"/>
    </svg>
    <div class="brand-name">Venture Kite</div>
    <div class="contacts">
      <div class="contact">
        <div class="contact__name">Ha Min Park</div>
        <div class="contact__line">Project Leader</div>
        <div class="contact__line">04 7720 3941</div>
        <div class="contact__line">ha-min.park@corvalaktrb.org</div>
      </div>
      <div class="contact">
        <div class="contact__name">Thomas Leung</div>
        <div class="contact__line">Vice Project Leader</div>
        <div class="contact__line">0479352806</div>
        <div class="contact__line">thomas.leung@corvalaktrb.org</div>
      </div>
    </div>
    <div class="website">www.corvalaktrb.org</div>
  </section>
</body>
</html>
```